Wirenexa

I'm looking to much improve our current website wirenexa.com
Updates

Low design quality

Target Market(s)

Commercial clients (Not-Residentials)

Industry/Entity Type

Office buildings and Industrial clients

Coding

Coded - Design and coding required

Number of Pages Required

5+ page

Requirements
Must have
• Very professional structured low voltage cabling projects for Wi-Fi, Audio/Video conference rooms, Access Control systems, CCTV.

```html
<!DOCTYPE html>
<html lang="en">
<head>
<meta charset="utf-8">
<title>Wirenexa — Commercial Infrastructure</title>
<link href="https://fonts.googleapis.com/css2?family=Space+Grotesk:wght@500;600;700&family=Inter:wght@400;500;600;700&family=JetBrains+Mono:wght@400;500;700&display=swap" rel="stylesheet">
<style>
:root{
  --red:#c2121c;
  --red-soft:#fbe9ea;
  --ink:#1c1f22;
  --dark:#1a1d20;
  --text:#4a4f55;
  --muted:#6b7178;
  --line:#e3e5e8;
  --page:#f8f9fa;
  --band:#f1f2f4;
  --white:#ffffff;
}
*{box-sizing:border-box;margin:0;padding:0}
html,body{width:1200px;height:3226px;overflow:hidden}
body{background:var(--page);font-family:"Inter",sans-serif;color:var(--ink);position:relative}
.abs{position:absolute}
.mono{font-family:"JetBrains Mono",monospace}
.display{font-family:"Space Grotesk",sans-serif}

/* nav */
.nav{left:0;top:0;width:1200px;height:50px;border-bottom:1px solid var(--line);background:var(--page)}
.brand{display:flex;align-items:center;gap:6px;font-family:"Space Grotesk",sans-serif;font-weight:700;font-size:22px;color:var(--red);letter-spacing:-0.5px}
.brand .mark{width:16px;height:16px;background:var(--red)}
.nav .brand{left:131px;top:12px}
.nav-links{left:463px;top:17px;display:flex;gap:27px;font-size:13px;color:var(--text)}
.nav-phone{left:840px;top:17px;font-size:12px;color:var(--text);display:flex;align-items:center;gap:5px}
.btn-quote{left:968px;top:14px;width:100px;height:22px;background:var(--red);color:#fff;font-size:10px;font-weight:700;letter-spacing:.8px;display:flex;align-items:center;justify-content:center}

/* hero */
.tag{left:131px;top:146px;height:21px;padding:0 10px;background:var(--red-soft);border-left:3px solid var(--red);color:var(--red);font-size:10.5px;letter-spacing:.5px;display:flex;align-items:center}
.hero-title{left:131px;top:186px;width:400px;font-size:38px;font-weight:600;line-height:47px;letter-spacing:-0.5px}
.hero-copy{left:131px;top:298px;width:370px;font-size:14.5px;line-height:22.5px;color:var(--text)}
.btn{height:35px;display:flex;align-items:center;justify-content:center;font-size:10.5px;font-weight:700;letter-spacing:1px}
.btn-dark{left:131px;top:398px;width:143px;background:var(--dark);color:#fff}
.btn-line{left:287px;top:398px;width:140px;border:1.5px solid #c9ccd0;color:var(--ink)}
.hero-frame{left:505px;top:354px;width:149px;height:150px;border:1px solid #f0b9bd}
.hero-photo{left:530px;top:100px;width:538px;height:268px;background:linear-gradient(105deg,#0f1a22 0%,#1f5f80 30%,#2c86ad 50%,#173544 70%,#0c1116 100%)}
.callback{left:530px;top:382px;width:538px;height:96px;background:var(--dark);color:#fff}
.callback h3{position:absolute;left:18px;top:22px;font-size:14.5px;font-weight:700}
.field-dark{position:absolute;top:56px;width:178px;height:24px;border-bottom:1px solid #4b5056;font-size:12.5px;color:#c7cace}
.btn-call{position:absolute;left:400px;top:47px;width:119px;height:32px;background:var(--red);font-size:10px;font-weight:700;letter-spacing:.8px;display:flex;align-items:center;justify-content:center}

/* stats */
.stats{left:131px;top:542px;width:937px;height:112px;border-top:1px solid var(--line);border-bottom:1px solid var(--line)}
.stat{position:absolute;top:34px}
.stat .label{font-size:10.5px;letter-spacing:.6px;color:var(--text)}
.stat .value{margin-top:6px;font-family:"Space Grotesk",sans-serif;font-size:25px;font-weight:600;color:var(--red)}
.stat-rule{position:absolute;top:31px;width:1px;height:50px;background:var(--line)}

/* services */
.services{left:0;top:716px;width:1200px;height:1002px;background:var(--band)}
.eyebrow{font-size:11px;letter-spacing:.8px;color:var(--red)}
.section-title{font-family:"Space Grotesk",sans-serif;font-size:25px;font-weight:500;letter-spacing:-0.2px}
.card{background:var(--white);border:1px solid #e6e8eb}
.card .icon{position:absolute;left:25px;top:25px;width:38px;height:38px;border:1px solid var(--line);display:flex;align-items:center;justify-content:center}
.card .badge{position:absolute;right:24px;top:29px;font-size:10.5px;font-weight:500;letter-spacing:.6px;color:var(--red)}
.card .name{position:absolute;left:25px;bottom:43px;font-family:"Space Grotesk",sans-serif;font-size:19px;font-weight:500}
.card .sub{position:absolute;left:25px;bottom:25px;font-size:8.5px;letter-spacing:.6px;color:var(--muted)}
.feature{left:131px;top:931px;width:618px;height:456px;background:linear-gradient(120deg,#e7e9eb 0%,#dfe2e3 40%,#d8dcdc 70%,#e2e3e0 100%)}
.feature .chip{position:absolute;left:32px;top:295px;height:18px;padding:0 7px;background:var(--red);color:#fff;font-size:10px;font-weight:700;letter-spacing:.5px;display:flex;align-items:center}
.feature h3{position:absolute;left:32px;top:324px;font-family:"Space Grotesk",sans-serif;font-size:19.5px;font-weight:500}
.feature p{position:absolute;left:32px;top:357px;width:360px;font-size:12.5px;line-height:19px;color:var(--text)}
.feature .ticks{position:absolute;left:32px;top:411px;display:flex;gap:26px;font-size:9.5px;letter-spacing:.4px;color:var(--ink)}
.ticks span{display:flex;align-items:center;gap:5px}

/* cases */
.case-photo{width:459px;height:286px}
.case-title{font-family:"Space Grotesk",sans-serif;font-size:19px;font-weight:500}
.case-desc{font-size:13px;color:var(--text)}
.case-tag{height:22px;padding:0 9px;border:1px solid #f0c4c7;color:var(--red);font-size:10px;letter-spacing:.6px;display:flex;align-items:center;background:var(--white)}

/* estimate */
.estimate{left:131px;top:2376px;width:937px;height:357px;background:linear-gradient(112deg,var(--dark) 0%,var(--dark) 76%,#2a1a1c 76.1%,#2b1719 100%);color:#fff}
.estimate h2{position:absolute;left:63px;top:92px;font-family:"Space Grotesk",sans-serif;font-size:25px;font-weight:600}
.estimate p{position:absolute;left:63px;top:137px;width:365px;font-size:13px;line-height:19px;color:#cfd2d6}
.estimate .points{position:absolute;left:63px;top:222px;font-size:11px;font-weight:500;letter-spacing:.6px;line-height:31px}
.points div{display:flex;align-items:center;gap:10px}
.form{position:absolute;left:479px;top:64px;width:396px;height:231px;background:var(--white);border-top:3px solid var(--red);color:var(--ink)}
.form label{position:absolute;font-size:9.5px;font-weight:700;letter-spacing:.6px}
.form .fline{position:absolute;height:1px;background:var(--line)}
.form .select{position:absolute;left:25px;top:122px;width:346px;height:30px;border-bottom:1px solid var(--line);font-size:12.5px;display:flex;justify-content:space-between;align-items:flex-start}
.form .submit{position:absolute;left:25px;top:169px;width:346px;height:35px;background:var(--red);color:#fff;font-size:10.5px;font-weight:700;letter-spacing:1px;display:flex;align-items:center;justify-content:center}

/* footer */
.footer{left:0;top:2827px;width:1200px;height:399px;border-top:1px solid var(--line);background:var(--page)}
.footer .brand{position:absolute;left:131px;top:69px}
.foot-about{left:131px;top:113px;width:230px;font-size:12.5px;line-height:19px;color:var(--text)}
.socials{left:131px;top:213px;display:flex;gap:9px}
.socials span{width:32px;height:32px;border:1px solid var(--line);background:var(--white);display:flex;align-items:center;justify-content:center}
.socials span i{width:10px;height:10px;border-radius:50%;background:var(--ink);display:block}
.fcol h4{font-size:10px;font-weight:700;letter-spacing:.8px;margin-bottom:11px}
.fcol li{list-style:none;font-size:13px;color:var(--text);line-height:19px;margin-bottom:9px}
.fcol .ic{display:flex;gap:7px}
.foot-bottom{left:100px;top:305px;width:1000px;border-top:1px solid var(--line)}
.copy{left:131px;top:325px;font-size:9.5px;color:var(--muted);letter-spacing:.3px}
.site{left:1000px;top:325px;width:68px;text-align:right;font-size:9.5px;color:var(--red);font-weight:700}
</style>
</head>
<body>

<header class="nav abs">
  <div class="brand abs"><span class="mark"></span>Wirenexa</div>
  <nav class="nav-links abs">
    <span>Services&nbsp;<svg width="8" height="8" viewBox="0 0 10 10"><path d="M2 3.5 5 6.5 8 3.5" fill="none" stroke="#4a4f55" stroke-width="1.4"/></svg></span>
    <span>Projects</span><span>About</span><span>Contact</span>
  </nav>
  <div class="nav-phone abs mono">
    <svg width="11" height="11" viewBox="0 0 24 24"><path d="M6.6 10.8a15 15 0 0 0 6.6 6.6l2.2-2.2c.3-.3.7-.4 1-.2 1.1.4 2.3.6 3.6.6.6 0 1 .4 1 1V20c0 .6-.4 1-1 1A17 17 0 0 1 3 4c0-.6.4-1 1-1h3.5c.6 0 1 .4 1 1 0 1.3.2 2.5.6 3.6.1.3 0 .7-.2 1z" fill="#c2121c"/></svg>
    (888) 555-0142
  </div>
  <div class="btn-quote abs">GET QUOTE</div>
</header>

<section class="hero">
  <div class="tag abs mono">COMMERCIAL INFRASTRUCTURE</div>
  <h1 class="hero-title abs display">Reliable Connectivity for Your Business.</h1>
  <p class="hero-copy abs">Premium low-voltage engineering for modern offices and high-output warehouses. We move your business from legacy wires to integrated technology solutions.</p>
  <div class="btn btn-dark abs">START ESTIMATE</div>
  <div class="btn btn-line abs">VIEW PROJECTS</div>
  <div class="hero-frame abs"></div>
  <div class="hero-photo abs" role="img" aria-label="Server rack with bundles of blue network cables"></div>
  <div class="callback abs">
    <h3>Request a Callback</h3>
    <div class="field-dark" style="left:18px">Your Name</div>
    <div class="field-dark" style="left:209px">Phone Number</div>
    <div class="btn-call">REQUEST CALL</div>
  </div>
</section>

<section class="stats abs">
  <div class="stat" style="left:0"><div class="label mono">RELIABILITY</div><div class="value">30yr Warranty</div></div>
  <div class="stat-rule" style="left:221px"></div>
  <div class="stat" style="left:265px"><div class="label mono">QUALITY ASSURANCE</div><div class="value">Field Certified</div></div>
  <div class="stat-rule" style="left:459px"></div>
  <div class="stat" style="left:504px"><div class="label mono">STANDARD</div><div class="value">10Gbps Ready</div></div>
  <div class="stat-rule" style="left:698px"></div>
  <div class="stat" style="left:742px"><div class="label mono">EXPERIENCE</div><div class="value">500+ Projects</div></div>
</section>

<section class="services abs">
  <div class="eyebrow mono abs" style="left:131px;top:95px">TECHNICAL SERVICES</div>
  <h2 class="section-title abs" style="left:131px;top:120px">Commercial Infrastructure Solutions</h2>
  <p class="abs" style="left:769px;top:96px;width:305px;font-size:13px;line-height:19px;color:var(--text)">Engineered systems designed to scale with your growing business needs, from physical cabling to intelligent analytics.</p>
</section>

<article class="feature abs" role="img" aria-label="Soft background of bundled blue and yellow structured cables">
  <div class="chip">CAT6A / FIBER</div>
  <h3>Structured Cabling</h3>
  <p>Copper and single-mode fiber backbones for warehouse distribution and multi-floor office campuses.</p>
  <div class="ticks mono">
    <span><svg width="10" height="10" viewBox="0 0 10 10"><path d="M1.5 5.2 4 7.5 8.5 2.5" fill="none" stroke="#c2121c" stroke-width="1.4"/></svg>LIFETIME SUPPORT</span>
    <span><svg width="10" height="10" viewBox="0 0 10 10"><path d="M1.5 5.2 4 7.5 8.5 2.5" fill="none" stroke="#c2121c" stroke-width="1.4"/></svg>CERTIFIED TESTING</span>
  </div>
</article>

<article class="card abs" style="left:769px;top:931px;width:299px;height:218px">
  <div class="icon"><svg width="16" height="16" viewBox="0 0 24 24" fill="none" stroke="#c2121c" stroke-width="2"><rect x="2" y="6" width="14" height="12" rx="1"/><path d="M16 10l6-3v10l-6-3z"/></svg></div>
  <div class="badge mono">AI ANALYTICS</div>
  <div class="name">Video Surveillance</div>
  <div class="sub mono">CCTV &amp; INTELLIGENT TRACKING</div>
</article>

<article class="card abs" style="left:769px;top:1169px;width:299px;height:218px">
  <div class="icon"><svg width="16" height="16" viewBox="0 0 24 24" fill="none" stroke="#c2121c" stroke-width="2"><rect x="5" y="11" width="14" height="10" rx="1"/><path d="M8 11V7a4 4 0 0 1 8 0v4"/><circle cx="12" cy="16" r="1.2" fill="#c2121c"/></svg></div>
  <div class="badge mono">BIOMETRIC</div>
  <div class="name">Access Control</div>
  <div class="sub mono">KEYCARD &amp; MOBILE ENTRY</div>
</article>

<article class="card abs" style="left:131px;top:1407px;width:300px;height:218px">
  <div class="icon"><svg width="16" height="16" viewBox="0 0 24 24" fill="none" stroke="#c2121c" stroke-width="2.2"><path d="M2 9a15 15 0 0 1 20 0M5.5 12.5a10 10 0 0 1 13 0M9 16a5 5 0 0 1 6 0"/><circle cx="12" cy="19.5" r="1.2" fill="#c2121c"/></svg></div>
  <div class="badge mono">HIGH-DENSITY</div>
  <div class="name">Wireless Access</div>
  <div class="sub mono">MESH &amp; DEDICATED WAP</div>
</article>

<article class="card abs" style="left:450px;top:1407px;width:299px;height:218px">
  <div class="icon"><svg width="16" height="16" viewBox="0 0 24 24" fill="none" stroke="#c2121c" stroke-width="2"><rect x="9" y="9" width="6" height="6" transform="rotate(45 12 12)"/><path d="M5 5l4 4M15 15l4 4M3 21c0-3 2-5 5-5"/></svg></div>
  <div class="badge mono">PROFESSIONAL</div>
  <div class="name">Satellite Install</div>
  <div class="sub mono">CUSTOM ROOF &amp; POLE MOUNTS</div>
</article>

<article class="card abs" style="left:769px;top:1407px;width:299px;height:218px">
  <div class="icon"><svg width="16" height="16" viewBox="0 0 24 24" fill="none" stroke="#c2121c" stroke-width="2"><rect x="2" y="5" width="15" height="11" rx="1"/><rect x="14" y="9" width="8" height="11" rx="1" fill="#fff"/><path d="M6 20h6"/></svg></div>
  <div class="name">POS Systems</div>
  <div class="sub mono">TERMINAL NETWORKING</div>
</article>

<section class="cases">
  <div class="eyebrow mono abs" style="left:0;width:1200px;text-align:center;top:1813px">CASE STUDIES</div>
  <h2 class="section-title abs" style="left:0;width:1200px;text-align:center;top:1838px">Built for SMBs. Certified for Growth.</h2>

  <div class="case-photo abs" style="left:131px;top:1934px;background:linear-gradient(90deg,#cfcfcf 0%,#9a9a9a 40%,#e8e8e8 70%,#7a7a7a 100%)" role="img" aria-label="Bright minimalist office with desk and chair, black and white"></div>
  <div class="case-title abs" style="left:131px;top:2239px">Tech District HQ</div>
  <div class="case-desc abs" style="left:131px;top:2264px">Full-floor Cat6e deployment with high-density WAP configuration.</div>
  <div class="case-tag mono abs" style="left:531px;top:2239px">OFFICE</div>

  <div class="case-photo abs" style="left:610px;top:1934px;background:linear-gradient(180deg,#6e6e6e 0%,#3d3d3d 30%,#5c5c5c 60%,#8b8b8b 100%)" role="img" aria-label="Empty industrial warehouse with steel columns, black and white"></div>
  <div class="case-title abs" style="left:610px;top:2239px">Logistics Hub A</div>
  <div class="case-desc abs" style="left:610px;top:2264px">AI-driven security integration and long-range fiber networking.</div>
  <div class="case-tag mono abs" style="left:988px;top:2239px">WAREHOUSE</div>
</section>

<section class="estimate abs">
  <h2>Get a Precision Estimate.</h2>
  <p>Our technical leads will review your floor plans and provide a comprehensive line-item quote tailored to your SMB requirements.</p>
  <div class="points mono">
    <div><svg width="11" height="11" viewBox="0 0 10 10"><path d="M5 0v10M0 5h10" stroke="#c2121c" stroke-width="1.4"/></svg>PROJECT SCOPING IN 24H</div>
    <div><svg width="11" height="11" viewBox="0 0 10 10"><path d="M5 0v10M0 5h10" stroke="#c2121c" stroke-width="1.4"/></svg>NO-HIDDEN-FEE GUARANTEE</div>
  </div>
  <div class="form">
    <label style="left:25px;top:33px">FULL NAME</label>
    <div class="fline" style="left:25px;top:78px;width:164px"></div>
    <label style="left:208px;top:33px">COMPANY</label>
    <div class="fline" style="left:208px;top:78px;width:163px"></div>
    <label style="left:25px;top:105px">SERVICE REQUIREMENT</label>
    <div class="select"><span>Structured Cabling</span><svg width="12" height="12" viewBox="0 0 10 10"><path d="M2 3.5 5 6.5 8 3.5" fill="none" stroke="#1c1f22" stroke-width="1.3"/></svg></div>
    <div class="submit">SUBMIT FOR REVIEW</div>
  </div>
</section>

<footer class="footer abs">
  <div class="brand"><span class="mark"></span>Wirenexa</div>
  <p class="foot-about abs">Technical infrastructure specialists providing white-glove cabling and security solutions for the commercial sector.</p>
  <div class="socials abs">
    <span aria-label="Social profile"><i></i></span>
    <span aria-label="Social profile"><i></i></span>
    <span aria-label="Social profile"><i></i></span>
    <span aria-label="Social profile"><i></i></span>
    <span aria-label="Social profile"><i></i></span>
  </div>
  <div class="fcol abs" style="left:371px;top:62px">
    <h4>SERVICES</h4>
    <ul>
      <li>Structured Cabling (Copper &amp; Fiber)</li><li>Video Surveillance / CCTV</li><li>Access Control</li><li>Wireless Access Points (WAP)</li><li>Point of Sale (POS)</li><li>Satellite Internet</li><li>Conference Room Technology</li>
    </ul>
  </div>
  <div class="fcol abs" style="left:610px;top:62px">
    <h4>COMPANY</h4>
    <ul><li>About</li><li>Portfolio</li><li>Services</li><li>Get an Estimate</li></ul>
  </div>
  <div class="fcol abs" style="left:769px;top:62px;width:130px">
    <h4>CERTIFICATIONS</h4>
    <ul style="padding-left:11px">
      <li>Certiva CX-8000 Certified</li><li>CablePro Guild Member</li><li>ANSI/TIA-568 Compliant</li><li>30-Year System Warranty</li>
    </ul>
  </div>
  <div class="fcol abs" style="left:928px;top:62px;width:170px">
    <h4>CONTACT HQ</h4>
    <ul>
      <li class="ic"><svg width="13" height="13" viewBox="0 0 24 24" style="margin-top:3px;flex:none"><path d="M12 2a7 7 0 0 0-7 7c0 5 7 13 7 13s7-8 7-13a7 7 0 0 0-7-7z" fill="none" stroke="#c2121c" stroke-width="2"/><circle cx="12" cy="9" r="2.5" fill="#c2121c"/></svg><span>1420 Harbor Point Dr, Suite 310<br>Arlington, VA 22201</span></li>
      <li class="ic" style="margin-top:-4px"><svg width="13" height="13" viewBox="0 0 24 24" style="margin-top:3px;flex:none"><path d="M6.6 10.8a15 15 0 0 0 6.6 6.6l2.2-2.2c.3-.3.7-.4 1-.2 1.1.4 2.3.6 3.6.6.6 0 1 .4 1 1V20c0 .6-.4 1-1 1A17 17 0 0 1 3 4c0-.6.4-1 1-1h3.5c.6 0 1 .4 1 1 0 1.3.2 2.5.6 3.6.1.3 0 .7-.2 1z" fill="#c2121c"/></svg>703-555-0187</li>
      <li class="ic" style="margin-top:-4px"><svg width="13" height="13" viewBox="0 0 24 24" style="margin-top:3px;flex:none"><path d="M6.6 10.8a15 15 0 0 0 6.6 6.6l2.2-2.2c.3-.3.7-.4 1-.2 1.1.4 2.3.6 3.6.6.6 0 1 .4 1 1V20c0 .6-.4 1-1 1A17 17 0 0 1 3 4c0-.6.4-1 1-1h3.5c.6 0 1 .4 1 1 0 1.3.2 2.5.6 3.6.1.3 0 .7-.2 1z" fill="#c2121c"/></svg>(888) 555-0142</li>
      <li class="ic" style="margin-top:-4px"><svg width="13" height="13" viewBox="0 0 24 24" style="margin-top:3px;flex:none"><rect x="3" y="5" width="18" height="14" rx="1" fill="none" stroke="#c2121c" stroke-width="2"/><path d="M3 6l9 7 9-7" fill="none" stroke="#c2121c" stroke-width="2"/></svg>sales@wirenexa.com</li>
    </ul>
  </div>
  <div class="foot-bottom abs"></div>
  <div class="copy abs mono">© 2026 Wirenexa Technical Solutions. All rights reserved.</div>
  <div class="site abs mono">wirenexa.com</div>
</footer>

</body>
</html>
```